Construction company yard sign

I would like a design for yard signs for my construction company. It will be used to put outside clients homes as we are working for them and will be used as advertisement for neighbors that are passing by the home.

The sign will be 18x24 and a plastic type material.

Target Market(s)

Homeowners

Font styles to use
Sans Serif

Requirements
Must have
• The most important thing about the sign is the visibility of the lettering and phone number 520-555-0147. The next would be Free roof Inspections. and then I would like to have these 3 words on there as well: Flat - Shingle - Tile

```html
<!DOCTYPE html>
<html lang="en">
<head>
<meta charset="utf-8">
<title>Halden Construction Group – Yard Sign</title>
<link href="https://fonts.googleapis.com/css2?family=Montserrat:wght@700;800;900&family=Oswald:wght@600;700&display=swap" rel="stylesheet">
<style>
  :root {
    --white: #ffffff;
    --brand-blue: #2a9fd8;
    --sign-red: #c81f2e;
    --free-red: #e81c24;
    --band-blue: #1466d6;
    --band-blue-dark: #0d56bf;
    --sky: #4a8fe0;
    --roof: #3d3d42;
  }
  html, body {
    margin: 0;
    padding: 0;
    overflow: hidden;
    background: #f2f2f2;
  }
  .sign {
    position: relative;
    width: 1200px;
    height: 900px;
    overflow: hidden;
    background: var(--white);
    font-family: "Montserrat", sans-serif;
  }
  .header {
    position: absolute;
    left: 0; top: 0;
    width: 1200px; height: 186px;
    background: var(--white);
  }
  .brand {
    position: absolute;
    left: 44px; top: 38px;
    color: var(--brand-blue);
    font-family: "Montserrat", sans-serif;
    font-weight: 800;
    line-height: 1;
  }
  .brand-name {
    display: block;
    font-size: 74px;
    letter-spacing: 2px;
  }
  .brand-sub {
    display: block;
    margin-top: 10px;
    font-size: 22px;
    letter-spacing: 6.5px;
  }
  .services {
    position: absolute;
    right: 0; top: 0;
    width: 640px; height: 186px;
    background: var(--sign-red);
    clip-path: polygon(50px 0, 100% 0, 100% 100%, 0 100%);
    display: flex;
    align-items: center;
    justify-content: center;
    padding-left: 30px;
    box-sizing: border-box;
    color: var(--white);
    font-family: "Oswald", sans-serif;
    font-weight: 700;
    font-size: 66px;
    letter-spacing: 0.5px;
  }
  .services .dot {
    display: inline-block;
    width: 17px; height: 17px;
    margin: 0 12px;
    border-radius: 50%;
    background: var(--white);
    vertical-align: middle;
  }
  .photo {
    position: absolute;
    left: 0; top: 186px;
    width: 1200px; height: 534px;
    background:
      linear-gradient(160deg, rgba(0,0,0,0) 45%, rgba(30,30,35,0.35) 100%),
      linear-gradient(180deg, var(--sky) 0%, #6a8db5 30%, #5c5f66 55%, var(--roof) 100%);
  }
  .offer {
    position: absolute;
    left: 0; top: 186px;
    width: 1200px; height: 534px;
    text-align: center;
  }
  .offer-free {
    position: absolute;
    left: 0; right: 0; top: 150px;
    color: var(--free-red);
    font-weight: 900;
    font-size: 330px;
    line-height: 0.8;
    letter-spacing: -4px;
    transform: scaleX(0.88);
  }
  .offer-detail {
    position: absolute;
    left: 0; right: 0; top: 428px;
    color: var(--white);
    font-weight: 800;
    font-size: 72px;
    line-height: 1;
    letter-spacing: 1px;
  }
  .contact {
    position: absolute;
    left: 0; top: 720px;
    width: 1200px; height: 180px;
    background: linear-gradient(180deg, var(--band-blue) 0%, var(--band-blue-dark) 100%);
    display: flex;
    align-items: center;
    justify-content: center;
    gap: 34px;
  }
  .contact-icon {
    width: 124px; height: 124px;
  }
  .contact-phone {
    color: var(--white);
    font-family: "Oswald", sans-serif;
    font-weight: 600;
    font-size: 136px;
    line-height: 1;
    letter-spacing: 1px;
    margin-top: -8px;
  }
</style>
</head>
<body>
  <div class="sign">
    <header class="header">
      <div class="brand">
        <span class="brand-name">HALDEN</span>
        <span class="brand-sub">CONSTRUCTION GROUP</span>
      </div>
      <div class="services">Flat<span class="dot"></span>Shingle<span class="dot"></span>Tile</div>
    </header>

    <div class="photo" role="img" aria-label="Photo of a dark tiled house roof with a dormer window against a blue sky"></div>

    <section class="offer">
      <div class="offer-free">FREE</div>
      <div class="offer-detail">ROOF INSPECTIONS</div>
    </section>

    <footer class="contact">
      <svg class="contact-icon" viewBox="0 0 124 124" aria-hidden="true">
        <circle cx="62" cy="62" r="55" fill="none" stroke="#ffffff" stroke-width="8"/>
        <path fill="#ffffff" d="M44 32c3-2 6-1 8 2l7 11c2 3 1 6-1 8l-5 4c3 8 9 15 17 19l4-5c2-3 5-3 8-1l11 7c3 2 4 5 2 8l-4 6c-3 4-8 5-13 4-19-5-34-21-39-40-1-5 0-10 4-13z"/>
      </svg>
      <div class="contact-phone">520-555-0147</div>
    </footer>
  </div>
</body>
</html>
```